Electrical Contracting business card design

We need a simple business card design for an Electrical Contracting business. A simple design would be appreciated
This company has 2 directors so on one it would have Colin Marsh & another with Dana Marsh.
Updates

Reason: Hello A few designers have asked for a logo unfortunately we don't have one so have extended deadline to see who can help us out with this. CHEERS

Reason: Waiting for business partner to return from xmas break. cheers

Industry/Entity Type

Business

Contact Information for Business Card

Volmera Electrical Services P/L
REC: 36074
Residential Commercial Industrial
Service-Repairs-Renovations-Installations-Telephone-Data
Colin Marsh-Ph: 0433 517 862
Email: colin@volmeraelectrical.com.au

Requirements
Should not have
• The design should not have any electrical appliances in it ie: power-points, leads, houses etc.

```html
<!DOCTYPE html>
<html lang="en">
<head>
<meta charset="utf-8">
<title>Volmera Electrical Services – Business Cards</title>
<link rel="stylesheet" href="https://fonts.googleapis.com/css2?family=Lato:wght@300;400;700;900&display=swap">
<style>
  :root {
    --backdrop: #1c1c1e;
    --card-navy: #06204a;
    --ink-white: #ffffff;
    --ink-soft: #d9e0ec;
    --ink-muted: #5d6f8e;
    --rule-light: #c9d3e6;
  }
  * { margin: 0; padding: 0; box-sizing: border-box; }
  html, body {
    width: 1200px;
    height: 1000px;
    overflow: hidden;
    background: var(--backdrop);
    font-family: "Lato", sans-serif;
  }
  .canvas {
    position: relative;
    width: 1200px;
    height: 1000px;
  }
  .card {
    position: absolute;
    width: 540px;
    height: 330px;
    background: var(--card-navy);
    border-radius: 10px;
    box-shadow: 0 18px 40px rgba(0, 0, 0, 0.55);
    color: var(--ink-white);
  }

  /* Front card: brand + services */
  .card--front { left: 600px; top: 150px; }
  .brand {
    display: flex;
    align-items: center;
    gap: 12px;
  }
  .brand__square {
    width: 30px;
    height: 30px;
    background: var(--ink-white);
    flex: none;
  }
  .brand__name {
    font-weight: 900;
    font-size: 22px;
    line-height: 1.05;
    text-transform: uppercase;
    letter-spacing: 0.2px;
    white-space: nowrap;
  }
  .card--front .brand {
    position: absolute;
    left: 120px;
    top: 110px;
  }
  .services {
    position: absolute;
    left: 0;
    right: 0;
    top: 200px;
    text-align: center;
    font-size: 12.5px;
    font-weight: 400;
    color: var(--ink-soft);
    line-height: 1.55;
  }

  /* Back card: contact */
  .card--contact { left: 70px; top: 520px; }
  .card--contact .brand {
    position: absolute;
    left: 40px;
    top: 74px;
  }
  .card--contact .brand__name { font-size: 15px; }
  .card--contact .brand__square { width: 22px; height: 22px; }
  .card--contact .brand { gap: 10px; }
  .divider {
    position: absolute;
    left: 284px;
    top: 60px;
    width: 2px;
    height: 220px;
  }
  .contact {
    position: absolute;
    left: 306px;
    top: 150px;
  }
  .contact__name {
    font-size: 24px;
    font-weight: 400;
    margin-bottom: 10px;
    white-space: nowrap;
  }
  .contact__line {
    display: flex;
    align-items: center;
    gap: 9px;
    font-size: 14px;
    font-weight: 300;
    margin-bottom: 6px;
    white-space: nowrap;
  }
  .contact__icon { width: 13px; height: 13px; flex: none; }
  .licence {
    position: absolute;
    right: 26px;
    bottom: 18px;
    font-size: 11px;
    color: var(--ink-muted);
    letter-spacing: 0.5px;
  }
</style>
</head>
<body>
<main class="canvas">

  <section class="card card--front" aria-label="Business card front">
    <div class="brand">
      <span class="brand__square"></span>
      <span class="brand__name">Volmera Electrical<br>Services</span>
    </div>
    <p class="services">
      Residential Commercial Industrial Service<br>
      • Repairs • Renovations • Installations • Telephone • Data
    </p>
  </section>

  <section class="card card--contact" aria-label="Business card contact side">
    <div class="brand">
      <span class="brand__square"></span>
      <span class="brand__name">Volmera Electrical<br>Services</span>
    </div>

    <svg class="divider" viewBox="0 0 2 220" preserveAspectRatio="none" aria-hidden="true">
      <defs>
        <linearGradient id="divider-fade" x1="0" y1="0" x2="0" y2="1">
          <stop offset="0" stop-color="#c9d3e6" stop-opacity="0"/>
          <stop offset="0.5" stop-color="#c9d3e6" stop-opacity="1"/>
          <stop offset="1" stop-color="#c9d3e6" stop-opacity="0"/>
        </linearGradient>
      </defs>
      <rect width="2" height="220" fill="url(#divider-fade)"/>
    </svg>

    <div class="contact">
      <p class="contact__name">Colin Marsh</p>
      <p class="contact__line">
        <svg class="contact__icon" viewBox="0 0 24 24" aria-hidden="true">
          <path fill="#ffffff" d="M6.6 10.8a15.1 15.1 0 0 0 6.6 6.6l2.2-2.2a1 1 0 0 1 1-.25 11.4 11.4 0 0 0 3.6.57 1 1 0 0 1 1 1V20a1 1 0 0 1-1 1A17 17 0 0 1 3 4a1 1 0 0 1 1-1h3.5a1 1 0 0 1 1 1c0 1.25.2 2.45.57 3.57a1 1 0 0 1-.25 1z"/>
        </svg>
        0433 517 862
      </p>
      <p class="contact__line">
        <svg class="contact__icon" viewBox="0 0 24 24" aria-hidden="true">
          <path fill="#ffffff" d="M2 5h20v14H2z M3.5 6.5 12 13l8.5-6.5" stroke="#06204a" stroke-width="1.6"/>
        </svg>
        colin@volmeraelectrical.com.au
      </p>
    </div>

    <p class="licence">REC. 36074</p>
  </section>

</main>
</body>
</html>
```